Beauty spa price list booklet. 16 pages from front to rear. Mainly white with compay logo

I need an A6 sized booklet for a beauty day spa.To incorporate our company logo, stock beauty photos (massages, facials, will send some examples over shortly.)16 Pages from front to rear.

Text sent over to be incorporated into the design as similar as the example one I've sent your as you can. Uploaded stock photos to be used in the correct places (Ie waxing photo on the waxing page etc....)

I've sent over a lot of the menu text but:

***I WILL WRITE UP AND SEND OVER THE REST OF THE LUMA SPA TREATMENT TEXT IN THE NEXT DAY OR TWO!!***

Target Market(s)

Customers using the spa. to take it away and keep at home.

Font styles to use
Serif
Sans Serif

Colors
00a990
33a6d7
ffffff

Requirements
Must have
• Company logo. Price lists.
• We like the use of white (for the most part. And teal tones in places.)
• Clear professional text with a good layout.

```html
<!DOCTYPE html>
<html lang="en">
<head>
<meta charset="utf-8">
<title>Luma Spa – Waxing Price List</title>
<link href="https://fonts.googleapis.com/css2?family=Sorts+Mill+Goudy&display=swap" rel="stylesheet">
<style>
  :root {
    --teal: #00a990;
    --teal-text: #0aa38b;
    --sky: #33a6d7;
    --sky-soft: #bcdcef;
    --white: #ffffff;
    --logo-ink: #2c5f86;
    --photo-warm: #c99a7c;
    --photo-deep: #8a6350;
  }
  * { margin: 0; padding: 0; box-sizing: border-box; }
  html, body { width: 1200px; height: 851px; overflow: hidden; background: var(--white); }
  .page {
    position: relative;
    width: 1200px;
    height: 851px;
    overflow: hidden;
    background: var(--white);
    font-family: "Sorts Mill Goudy", "Goudy Old Style", Georgia, serif;
    color: var(--teal-text);
  }
  .page__wash { position: absolute; inset: 0; }

  .price-list { position: absolute; }
  .price-list__title {
    height: 47px;
    background: var(--teal);
    color: var(--white);
    font-weight: 400;
    font-size: 34px;
    line-height: 47px;
    text-align: center;
  }
  .price-list__items { list-style: none; padding: 3px 12px 0 12px; }
  .price-list__item {
    display: flex;
    justify-content: space-between;
    height: 48px;
    font-size: 34px;
    line-height: 48px;
  }
  .price-list--women { left: 151px; top: 65px; width: 468px; }
  .price-list--men { left: 649px; top: 550px; width: 464px; }

  .feature-photo {
    position: absolute;
    left: 651px;
    top: 0;
    width: 549px;
    height: 505px;
    background: var(--teal);
    padding: 0 0 9px 10px;
  }
  .feature-photo__fill {
    width: 100%;
    height: 100%;
    background: linear-gradient(135deg, #b58c74 0%, var(--photo-warm) 40%, #d9b398 65%, var(--photo-deep) 100%);
  }

  .brand {
    position: absolute;
    left: 65px;
    top: 637px;
    width: 134px;
    height: 134px;
    border-radius: 50%;
    background: var(--white);
    display: flex;
    align-items: center;
    justify-content: center;
  }
  .brand__name {
    font-size: 24px;
    color: var(--logo-ink);
    font-weight: 400;
  }
</style>
</head>
<body>
<main class="page">
  <svg class="page__wash" width="1200" height="851" viewBox="0 0 1200 851" aria-hidden="true">
    <defs>
      <linearGradient id="wash" x1="0" y1="0" x2="1" y2="0.3">
        <stop offset="0" stop-color="#ffffff"/>
        <stop offset="0.35" stop-color="#bcdcef"/>
        <stop offset="0.75" stop-color="#c6e1f1"/>
        <stop offset="1" stop-color="#eef6fb"/>
      </linearGradient>
    </defs>
    <path d="M0 0 C 20 330, 190 640, 494 851 L 0 851 Z" fill="url(#wash)"/>
  </svg>

  <section class="price-list price-list--women">
    <h2 class="price-list__title">Waxing</h2>
    <ul class="price-list__items">
      <li class="price-list__item"><span>Eyebrow</span><span>£12.00</span></li>
      <li class="price-list__item"><span>Lip and Chin</span><span>£7.00</span></li>
      <li class="price-list__item"><span>Full Face</span><span>£12.00</span></li>
      <li class="price-list__item"><span>Under Arm</span><span>£10.00</span></li>
      <li class="price-list__item"><span>Half Leg</span><span>£16.00</span></li>
      <li class="price-list__item"><span>Three Quarter Leg</span><span>£20.00</span></li>
      <li class="price-list__item"><span>Full Leg</span><span>£23.00</span></li>
    </ul>
  </section>

  <figure class="feature-photo">
    <div class="feature-photo__fill" role="img" aria-label="Photo of a facial skin treatment being carried out at the spa"></div>
  </figure>

  <section class="price-list price-list--men">
    <h2 class="price-list__title">Men’s Waxing</h2>
    <ul class="price-list__items">
      <li class="price-list__item"><span>Full Back</span><span>£25.00</span></li>
      <li class="price-list__item"><span>Chest</span><span>£22.00</span></li>
      <li class="price-list__item"><span>Half Back</span><span>£13.00</span></li>
      <li class="price-list__item"><span>Chest and Tummy</span><span>£25.00</span></li>
    </ul>
  </section>

  <div class="brand">
    <span class="brand__name">Luma Spa</span>
  </div>
</main>
</body>
</html>
```